Trade Show Banner "Calmwrightery"

1.7' x 3' vertical banner to complement trade show booth panels (3-panel tabletop booth attached). The word file (attached) is for text and not meant to imply design. We manage homeowner and condo associations that are run by volunteer boards of directors who already have full-time jobs or who may have no training in how to run an organization. It can be highly stressful and not very rewarding. We want this poster/banner to convey that feeling of stress along with a hope for relief and relaxation. Our logo is attached. The full logo is the top one in the file. You may also want to use the triangle (attached) in addition to or instead of the logo. Our corporate fonts are attached. Please let me know if you need additional information or if you feel like there is too much copy or any other thoughts or comments you have.

Target Market(s)

Volunteer boards of directors for homeowner and condo associations--all ages, genders, races, occupations.

Industry/Entity Type

Property Management

Other font styles liked:
• "Bright Harbor" is part of a trademark and should be in Mistral with the green from our logo

Requirements
Must have
• Simple, easy to read, don't clash with booth design
Nice to have
• convey the tension of stress contrasted with the feeling of relaxation and relief.

```html
<!DOCTYPE html>
<html lang="en">
<head>
<meta charset="utf-8">
<title>The Art of Calmwrightery for Board Members</title>
<link rel="stylesheet" href="https://fonts.googleapis.com/css2?family=Courgette&family=Dancing+Script:wght@600&family=Fira+Sans:ital,wght@0,400;0,600;1,500&family=Open+Sans:wght@700;800&display=swap">
<style>
  :root {
    --sage: #5f8d62;
    --sage-dark: #4d7a51;
    --leaf: #2f6d37;
    --maroon: #761a24;
    --navy: #1f2b5c;
    --paper: #ffffff;
    --room-light: #eeece8;
    --room-mid: #dcd8d0;
    --wicker: #c7b494;
    --shirt: #a9bccb;
    --denim: #2e3650;
  }
  * { box-sizing: border-box; margin: 0; padding: 0; }
  html, body { width: 1200px; height: 2273px; overflow: hidden; }
  body { background: var(--paper); font-family: "Fira Sans", sans-serif; }

  .banner { position: relative; width: 1200px; height: 2273px; overflow: hidden; background: var(--paper); }

  .banner__backdrop { position: absolute; left: 0; top: 0; width: 1200px; height: 1254px; background: var(--sage); }

  .banner__photo {
    position: absolute; left: 0; top: 1500px; width: 1200px; height: 773px;
    background:
      radial-gradient(ellipse 420px 230px at 330px 330px, rgba(169,188,203,0.95) 0%, rgba(169,188,203,0) 100%),
      radial-gradient(ellipse 360px 200px at 860px 560px, rgba(46,54,80,0.9) 0%, rgba(46,54,80,0) 100%),
      radial-gradient(ellipse 700px 420px at 380px 620px, rgba(199,180,148,1) 0%, rgba(199,180,148,0.6) 55%, rgba(199,180,148,0) 100%),
      linear-gradient(180deg, var(--paper) 0%, var(--room-light) 20%, var(--room-mid) 100%);
  }

  .brand-card {
    position: absolute; left: 379px; top: 45px; width: 439px; height: 197px;
    background: var(--paper); border-radius: 22px;
    display: flex; align-items: center; justify-content: center; gap: 18px;
  }
  .brand-card__mark { width: 34px; height: 34px; background: var(--maroon); flex: none; }
  .brand-card__name {
    font-family: "Fira Sans", sans-serif; font-weight: 600; color: var(--maroon);
    font-size: 36px; line-height: 1.15;
  }

  .headline { position: absolute; left: 0; width: 1200px; text-align: center; color: var(--paper); display: block; }
  .headline__lead {
    top: 278px; font-family: "Open Sans", sans-serif; font-weight: 800; font-size: 56px; line-height: 1.2;
    letter-spacing: 1px; text-shadow: 3px 3px 4px rgba(0,0,0,0.35);
  }
  .headline__title {
    top: 350px; font-family: "Courgette", cursive; font-size: 146px; line-height: 1;
    text-shadow: 4px 4px 5px rgba(0,0,0,0.35);
  }
  .headline__sub {
    top: 502px; font-family: "Open Sans", sans-serif; font-weight: 800; font-size: 54px; line-height: 1.2;
    text-shadow: 3px 3px 4px rgba(0,0,0,0.35);
  }
  .headline__sub em { font-family: "Courgette", cursive; font-style: normal; font-weight: 400; font-size: 56px; margin-right: 16px; }

  .stress-panel { position: absolute; left: 45px; top: 595px; width: 1111px; height: 980px; background: var(--paper); }

  .stress-card {
    position: absolute; border: 3px solid var(--sage-dark); background: var(--paper);
    padding: 18px 20px 0 24px;
  }
  .stress-card__problem {
    font-family: "Fira Sans", sans-serif; font-weight: 600; color: var(--maroon);
    font-size: 29px; line-height: 44px;
  }
  .stress-card__relief { color: var(--navy); font-size: 34px; line-height: 48px; margin-top: 8px; }
  .stress-card__relax { font-family: "Courgette", cursive; color: var(--leaf); font-size: 46px; }
  .trademark { font-family: "Dancing Script", cursive; font-weight: 600; color: var(--leaf); font-size: 38px; }

  .stress-card--workload { left: 64px; top: 618px; width: 521px; height: 243px; }
  .stress-card--issues { left: 615px; top: 618px; width: 521px; height: 243px; }
  .stress-card--payments { left: 64px; top: 891px; width: 521px; height: 331px; }
  .stress-card--communication { left: 615px; top: 891px; width: 521px; height: 331px; }
  .stress-card--delinquency { left: 64px; top: 1252px; width: 1072px; height: 296px; }

  .call-to-action { position: absolute; left: 620px; top: 1585px; width: 540px; text-align: center; }
  .call-to-action__lead {
    font-family: "Fira Sans", sans-serif; font-style: italic; font-weight: 500; color: var(--maroon);
    font-size: 47px; line-height: 50px; text-transform: uppercase;
  }
  .call-to-action__close { font-family: "Courgette", cursive; color: var(--leaf); font-size: 66px; line-height: 1.2; white-space: nowrap; }
</style>
</head>
<body>
<main class="banner">
  <div class="banner__backdrop"></div>
  <div class="banner__photo" role="img" aria-label="Photograph of a relaxed man leaning back with hands behind his head in a round wicker papasan chair in a bright room"></div>

  <div class="brand-card">
    <span class="brand-card__mark"></span>
    <span class="brand-card__name">Tallowmere<br>Management, Inc.</span>
  </div>

  <h1>
    <span class="headline headline__lead">THE ART OF</span>
    <span class="headline headline__title">Calmwrightery</span>
    <span class="headline headline__sub"><em>for</em>BOARD MEMBERS</span>
  </h1>

  <div class="stress-panel"></div>

  <section class="stress-card stress-card--workload">
    <p class="stress-card__problem">Stress: THE BOARD HAS TOO<br>MUCH WORK TO DO</p>
    <p class="stress-card__relief"><span class="stress-card__relax">Relax...</span> and let us do<br>the work.</p>
  </section>

  <section class="stress-card stress-card--issues">
    <p class="stress-card__problem">Stress: YOUR COMMUNITY<br>HAS “ISSUES.”</p>
    <p class="stress-card__relief"><span class="stress-card__relax">Relax...</span> and let us give<br>you a <span class="trademark">Bright Harbor.</span></p>
  </section>

  <section class="stress-card stress-card--payments">
    <p class="stress-card__problem">Stress: YOUR MEMBERS<br>CANNOT PAY ONLINE.</p>
    <p class="stress-card__relief"><span class="stress-card__relax">Relax...</span> we’ll give your<br>members multiple<br>ways to pay.</p>
  </section>

  <section class="stress-card stress-card--communication">
    <p class="stress-card__problem">Stress: COMMUNICATION IS<br>POOR OR INCONSISTENT.</p>
    <p class="stress-card__relief"><span class="stress-card__relax">Relax...</span> we’ll keep you<br>informed with a robust<br>online portal, chock full<br>of information.</p>
  </section>

  <section class="stress-card stress-card--delinquency">
    <p class="stress-card__problem">Stress: YOUR DELINQUENCIES ARE HIGH.</p>
    <p class="stress-card__relief"><span class="stress-card__relax">Relax...</span> as a licensed collection agency, we have<br>developed an effective collections program that works<br>in tandem with your collections attorney. Plus, we can<br>report to the credit bureau!</p>
  </section>

  <div class="call-to-action">
    <p class="call-to-action__lead">Come in to<br>talk and start</p>
    <p class="call-to-action__close">Relaxing Today!</p>
  </div>
</main>
</body>
</html>
```